Health & Nutrition - Business Cards

Needs to look new-age, simple, and elegant. The cards are for my services/counsel in health and nutrition - which include mind, body, and soul. I would like to see something clean and simple but beautiful. Can have a plain background or with a pattern but I don't want it to take away from my contact details. Therefore, my info can be on the back of the card and a nice front design. I really like the flower of life symbol. The name of my business is called Velvet Meadow.

Target Market(s)

Clients - men & women age 20-60. Adults, parents, teachers, sick individuals seeking nutrient counseling and dietary management.

Industry/Entity Type

Nutritionist

Contact Information for Business Card

Tomas Brindle
Cell: 345-827-4602
Email: tbrindle@quillpost.example

Colors
33a6d7
33b8a4
add136
ffffff
5c5c5c
f04a50
fbee3f
cedeed
85cae6

Requirements
Nice to have
• Maybe it can have some sort of sacred geometry as well, but not required. Nice to have the colors that I choose in the project but feel free to come up with your own use of colors. Thanks! =)

```html
<!DOCTYPE html>
<html lang="en">
<head>
<meta charset="utf-8">
<title>Velvet Meadow – Business Cards</title>
<link rel="stylesheet" href="https://fonts.googleapis.com/css2?family=Marcellus&family=Arimo:wght@400;700&display=swap">
<style>
  :root {
    --page: #e9ecef;
    --sky: #33a6d7;
    --teal: #33b8a4;
    --lime: #add136;
    --white: #ffffff;
    --ink: #111111;
    --grey: #5c5c5c;
    --card-w: 640px;
    --card-h: 366px;
  }
  * { box-sizing: border-box; margin: 0; padding: 0; }
  html, body {
    width: 1200px; height: 896px; overflow: hidden;
    background: var(--page);
  }
  .sheet {
    position: relative; width: 1200px; height: 896px;
    display: flex; flex-direction: column; align-items: center;
    justify-content: center; gap: 56px;
  }
  .card {
    position: relative; width: var(--card-w); height: var(--card-h);
    border-radius: 22px; overflow: hidden;
    box-shadow: 0 10px 28px rgba(0,0,0,0.18);
  }

  /* Front */
  .card-front {
    background: linear-gradient(200deg, var(--lime) 0%, var(--teal) 55%, var(--sky) 100%);
  }
  .front-decoration {
    position: absolute; right: -40px; top: -70px;
    width: 330px; height: 330px;
  }
  .front-brand {
    position: absolute; left: 0; right: 0; top: 118px;
    display: flex; flex-direction: column; align-items: center; gap: 14px;
    color: var(--white);
  }
  .brand-mark { width: 96px; height: 96px; }
  .brand-name {
    font-family: "Marcellus", serif; font-size: 34px;
    letter-spacing: 2px; text-transform: uppercase; line-height: 1;
  }
  .brand-tagline {
    font-family: "Marcellus", serif; font-size: 13px;
    letter-spacing: 2.5px; text-transform: uppercase; margin-top: -6px;
  }

  /* Back */
  .card-back { background: var(--white); color: var(--ink); }
  .back-brand {
    position: absolute; left: 34px; top: 56px;
  }
  .back-brand .brand-name { font-size: 30px; color: var(--ink); }
  .back-brand .brand-tagline { font-size: 12px; color: var(--ink); margin-top: 4px; }
  .back-decoration {
    position: absolute; right: -34px; top: -22px;
    width: 330px; height: 330px;
  }
  .contact {
    position: absolute; left: 36px; bottom: 44px;
    font-family: "Arimo", sans-serif;
  }
  .contact-name {
    font-family: "Marcellus", serif; font-size: 24px;
    letter-spacing: 1.5px; text-transform: uppercase; margin-bottom: 8px;
  }
  .contact-line { font-size: 16px; line-height: 1.45; color: var(--ink); }
</style>
</head>
<body>
<main class="sheet">

  <section class="card card-front" aria-label="Card front">
    <svg class="front-decoration" viewBox="0 0 330 330" role="img" aria-label="Faint large sacred geometry motif">
      <circle cx="165" cy="165" r="160" fill="#ffffff" fill-opacity="0.14"/>
    </svg>
    <div class="front-brand">
      <svg class="brand-mark" viewBox="0 0 96 96" aria-hidden="true">
        <circle cx="48" cy="48" r="44" fill="none" stroke="#ffffff" stroke-width="3"/>
      </svg>
      <div class="brand-name">Velvet Meadow</div>
      <div class="brand-tagline">Health and Nutrition</div>
    </div>
  </section>

  <section class="card card-back" aria-label="Card back">
    <div class="back-brand">
      <div class="brand-name">Velvet Meadow</div>
      <div class="brand-tagline">Health and Nutrition</div>
    </div>
    <svg class="back-decoration" viewBox="0 0 330 330" role="img" aria-label="Large black sacred geometry motif within a double ring">
      <circle cx="165" cy="165" r="160" fill="none" stroke="#111111" stroke-width="6"/>
      <circle cx="165" cy="165" r="146" fill="#111111"/>
    </svg>
    <div class="contact">
      <div class="contact-name">Tomas Brindle</div>
      <div class="contact-line">C: 345-827-4602</div>
      <div class="contact-line">E: tbrindle@quillpost.example</div>
    </div>
  </section>

</main>
</body>
</html>
```